Rework of Honey Labels - Updated for clarity

I am looking for a re-do of our current creamed honey labels.
Creamed honey is a butter-consistency. There are 5 flavors - original, lavender, chocolate, lemon, cinnamon. We want for it to look sophisticated and luxurious. We want the labels to all be cohesive in this group, but to be able to easily tell the difference between the products by color or something quick besides just words to tell the difference in the product. The product will be an off-white/light amber - except for the chocolate which is the color of Cremoso. There are three size containers for each of these honeys. But we can just focus on the single size for this contest.
The honey market in our area is extremely competitive. Right now, I feel our labels look more homemade. I want something that stands out. We charge a premium for our products. We want for our labels to look like we are a superior product. We are getting our product in many local stores and need to differentiate ourselves. I am attaching some of the labels that I think stand out. As for the labels themselves. They can include that whole blurb about us as Brookvale Meadow - or not. It is not truly necessary to have on the labels. But the logo needs to be included.
For all of these, we want something unique and special. Like you are going for an English mid-day tea at an upscale hotel in London with the Queen (well, I guess now the King...but really I think of the Queen).
I am uploading our current labels and then a few labels to take inspiration from.
Updates
I just reworked the description to be more limited in what I was asking for. Looking for a label for creamed honey in one size jar only. Thank you.

```html
<!DOCTYPE html>
<html lang="en">
<head>
<meta charset="UTF-8">
<title>Creamed Honey – Lemon Label</title>
<link rel="stylesheet" href="https://fonts.googleapis.com/css2?family=Bodoni+Moda:wght@400;500&family=Allura&family=Montserrat:wght@400&display=swap">
<style>
  :root {
    --page: #ffffff;
    --label-cream: #f7efe0;
    --label-light: #fbf6ec;
    --ink: #111111;
    --ink-soft: #333333;
    --lemon-band: #f7c300;
    --bee-gold: #d9a33a;
    --bee-dark: #3a3128;
    --wing: #e8e4dc;
  }
  * { margin: 0; padding: 0; box-sizing: border-box; }
  html, body {
    width: 1200px;
    height: 1200px;
    overflow: hidden;
    background: var(--page);
  }
  .canvas {
    position: relative;
    width: 1200px;
    height: 1200px;
    background: var(--page);
  }
  .label {
    position: absolute;
    left: 0;
    top: 158px;
    width: 1200px;
    height: 884px;
    background: linear-gradient(90deg, var(--label-cream) 0%, var(--label-light) 60%, var(--label-cream) 100%);
  }
  .bee-art {
    position: absolute;
    left: 434px;
    top: 106px;
    width: 332px;
    height: 220px;
    border-radius: 50%;
    background:
      radial-gradient(ellipse 18% 42% at 50% 58%, var(--bee-gold) 0%, var(--bee-dark) 70%, transparent 100%),
      radial-gradient(ellipse 50% 30% at 50% 35%, var(--wing) 0%, rgba(232,228,220,0) 100%);
  }
  .product-title {
    position: absolute;
    left: 0;
    top: 355px;
    width: 100%;
    text-align: center;
    font-family: "Bodoni Moda", "Didot", serif;
    font-weight: 500;
    font-size: 130px;
    line-height: 106px;
    letter-spacing: 2px;
    color: var(--ink);
  }
  .flavour-name {
    position: absolute;
    left: 0;
    top: 620px;
    width: 100%;
    text-align: center;
    font-family: "Allura", cursive;
    font-size: 110px;
    line-height: 120px;
    color: var(--ink);
    padding-right: 40px;
  }
  .flavour-band {
    position: absolute;
    left: 0;
    top: 764px;
    width: 100%;
    height: 12px;
    background: var(--lemon-band);
  }
  .net-weight {
    position: absolute;
    left: 0;
    top: 804px;
    width: 100%;
    text-align: center;
    font-family: "Montserrat", Arial, sans-serif;
    font-size: 30px;
    line-height: 40px;
    color: var(--ink-soft);
    padding-left: 12px;
  }
</style>
</head>
<body>
  <main class="canvas">
    <section class="label">
      <div class="bee-art" role="img" aria-label="Watercolour illustration of a honey bee with spread wings"></div>
      <h1 class="product-title">CREAMED<br>HONEY</h1>
      <p class="flavour-name">Lemon</p>
      <div class="flavour-band"></div>
      <p class="net-weight">-500 g -</p>
    </section>
  </main>
</body>
</html>
```